High-end residential home builder needs a business card design

We need a new business card design for a small residential construction company based in Boise, Idaho. We specialize in building custom high-end homes and remodels, with a focus on great design and craftsmanship.

We would like to use our current logo, but open to new color suggestions.
Just looking for a clean, sharp, modern design that looks high-end.

Target Market(s)

Upscale clientele

Industry/Entity Type

Contractor

Contact Information for Business Card

Company: Stonefield Custom Builders
Name: Marcus Tilley
Phone number: 208 367 4120
Email: MarcusTilleySCB@mailbox-example.com
Website: Stonefieldcustombuilders-example.com

Font styles to use
Serif
Sans Serif

Requirements
Must have
• Company Logo
Company name
My name
My phone number
My email
Company website
Nice to have
• I have attached a few photos of cards that I really like.

```html
<!DOCTYPE html>
<html lang="en">
<head>
<meta charset="utf-8">
<title>Stonefield Custom Builders – Business Card</title>
<link rel="stylesheet" href="https://fonts.googleapis.com/css2?family=Montserrat:wght@500&family=Poppins:wght@400;500&display=swap">
<style>
  :root {
    --backdrop: #d4d4d4;
    --card: #1b1b1b;
    --gold: #b8914b;
    --ink-light: #f4f4f4;
  }
  * { margin: 0; padding: 0; box-sizing: border-box; }
  html, body { width: 1200px; height: 1200px; overflow: hidden; }
  body {
    background: var(--backdrop);
    position: relative;
    font-family: "Poppins", sans-serif;
  }
  .card {
    position: absolute;
    left: 250px;
    width: 700px;
    height: 400px;
    background: var(--card);
  }
  .card--front { top: 150px; }
  .card--back { top: 650px; }

  .brand {
    position: absolute;
    inset: 0;
    display: flex;
    align-items: center;
    justify-content: center;
    gap: 26px;
  }
  .brand__square {
    width: 70px;
    height: 70px;
    border: 3px solid var(--gold);
  }
  .brand__name {
    font-family: "Montserrat", sans-serif;
    font-weight: 500;
    font-size: 24px;
    letter-spacing: 4px;
    text-transform: uppercase;
    color: var(--gold);
  }

  .holder-name {
    position: absolute;
    left: 60px;
    top: 56px;
    font-size: 30px;
    font-weight: 400;
    letter-spacing: 1px;
    text-transform: uppercase;
    color: var(--gold);
  }
  .contact {
    position: absolute;
    left: 60px;
    top: 190px;
    list-style: none;
    color: var(--ink-light);
    font-size: 17px;
    line-height: 30px;
  }
  .contact__phone { font-size: 22px; font-weight: 500; }
  .back-mark {
    position: absolute;
    right: 50px;
    bottom: 60px;
    width: 70px;
    height: 70px;
    border: 3px solid var(--gold);
  }
</style>
</head>
<body>
  <section class="card card--front">
    <div class="brand">
      <div class="brand__square"></div>
      <span class="brand__name">Stonefield Custom Builders</span>
    </div>
  </section>

  <section class="card card--back">
    <h1 class="holder-name">Marcus Tilley</h1>
    <ul class="contact">
      <li class="contact__company">Stonefield Custom Builders</li>
      <li class="contact__phone">208 367 4120</li>
      <li class="contact__email">MarcusTilleySCB@mailbox-example.com</li>
      <li class="contact__web">Stonefieldcustombuilders-example.com</li>
    </ul>
    <div class="back-mark"></div>
  </section>
</body>
</html>
```